Business card and stationary for a garage
Motorwerkplaats Lindeveld
@ph - changes done .Please check and confirm.- Thanks
@quickdraft
Can you please make another version with #136 as the front and #135 as the back side.
Note 1: Please omit the word "Services" and make the logo a little bit bigger at the back side
Note 2: It's Merelhoflaan
Note 3: #135 the back side. The text "Motorwerkplaats Lindeveld" is too gray. Just use the original logo and colors.
#ALL
Please use "T" for phonenumber and "F" for fax. Do not use the English abbreviations. Or better use icons.
Nice designs, thank you.
We dont prefer a style like #124-#129 for the back of the card. Its to simple. The service listing can be more attractive like in #121 or #118 (horizontal).
#ALL please do not use english words in business card like "Our services". Use only "Services" as this is also a common word in Dutch.
"Voor alle merken" means "For all brands"

```html
<!DOCTYPE html>
<html lang="nl">
<head>
<meta charset="utf-8">
<title>Motorwerkplaats Lindeveld – huisstijl</title>
<link href="https://fonts.googleapis.com/css2?family=Arimo:wght@400;700&display=swap" rel="stylesheet">
<style>
:root{
  --bg:#000;
  --paper:#fff;
  --red:#c4161c;
  --red-dark:#8c0d12;
  --red-light:#e33a3f;
  --ink:#2a2a2a;
  --grey-card:#6d6d6d;
  --grey-dark:#4a4a4a;
}
*{margin:0;padding:0;box-sizing:border-box}
html,body{width:1200px;height:742px;overflow:hidden;background:var(--bg)}
body{position:relative;font-family:"Arimo",Arial,sans-serif;color:var(--ink)}
.piece{position:absolute;overflow:hidden}
.piece svg.wave{position:absolute;left:0;width:100%}
.brand{display:flex;align-items:center;gap:6px;font-weight:700;color:var(--red);text-transform:uppercase;letter-spacing:.02em;line-height:1.05}
.brand .mark{flex:none;background:var(--red)}
.brand.on-dark{color:#fff}
.brand.on-dark .mark{background:#fff}

/* letterhead */
.letterhead{left:53px;top:19px;width:513px;height:677px;background:var(--paper)}
.letterhead .brand{position:absolute;left:22px;top:28px;font-size:19px;width:260px}
.letterhead .brand .mark{width:14px;height:14px}
.letterhead .wave{bottom:0;height:150px}
.letterhead .address{position:absolute;left:22px;bottom:22px;color:#fff;font-size:9.5px;line-height:1.45}

/* cards */
.card{border-radius:9px}
.card-front{left:576px;top:29px;width:216px;height:122px;background:var(--paper)}
.card-front .brand{position:absolute;left:12px;top:10px;font-size:8px;width:96px;gap:4px}
.card-front .brand .mark{width:6px;height:6px}
.card-front .person{position:absolute;right:14px;top:14px;font-size:8px;color:var(--red);font-weight:700;white-space:nowrap}
.card-front .contact{position:absolute;left:12px;top:46px;font-size:6px;line-height:1.45;color:var(--ink)}
.card-front .wave{bottom:0;height:42px}

.services{list-style:none;font-size:7.5px;line-height:1.4;text-align:center}
.services .all{margin-top:2px}

.card-red{left:679px;top:163px;width:214px;height:137px;background:radial-gradient(ellipse at 45% 30%,var(--red-light),var(--red) 50%,var(--red-dark));display:flex;flex-direction:column;align-items:center;justify-content:center;gap:12px;color:#fff}
.card-red .brand{font-size:11px;width:150px;justify-content:center;text-align:center}
.card-red .brand .mark{width:9px;height:9px}

.card-white{left:900px;top:77px;width:211px;height:127px;background:var(--paper);display:flex;flex-direction:column;align-items:center;justify-content:center;gap:12px;color:var(--ink)}
.card-white .brand{font-size:11px;width:150px;justify-content:center;text-align:center}
.card-white .brand .mark{width:9px;height:9px}

.card-grey{left:912px;top:228px;width:209px;height:127px;background:radial-gradient(ellipse at 50% 30%,#888,var(--grey-card) 55%,var(--grey-dark));display:flex;flex-direction:column;align-items:center;justify-content:center;gap:12px;color:#fff}
.card-grey .brand{font-size:11px;width:150px;justify-content:center;text-align:center}
.card-grey .brand .mark{width:9px;height:9px}

/* envelope */
.envelope{left:576px;top:365px;width:545px;height:331px;background:var(--paper)}
.envelope .flap{position:absolute;left:0;top:0;width:100%;height:140px}
.envelope .flap-name{position:absolute;left:0;right:0;top:26px;transform:rotate(180deg);justify-content:center;font-size:18px}
.envelope .flap-name .mark{width:12px;height:12px}
.envelope .sender{position:absolute;left:20px;top:150px;font-size:17px;width:250px}
.envelope .sender .mark{width:13px;height:13px}
.envelope .address{position:absolute;left:20px;top:258px;font-size:9px;line-height:1.45;color:var(--ink)}
.envelope .wave{bottom:0;height:70px}
</style>
</head>
<body>

<section class="piece letterhead" aria-label="Briefpapier">
  <div class="brand"><span class="mark"></span><span>Motorwerkplaats Lindeveld</span></div>
  <svg class="wave" viewBox="0 0 513 150" preserveAspectRatio="none" aria-hidden="true">
    <defs><linearGradient id="lhRed" x1="0" y1="0" x2="1" y2="1"><stop offset="0" stop-color="#d9262c"/><stop offset="1" stop-color="#8c0d12"/></linearGradient></defs>
    <path d="M0 20 C150 60 330 100 513 50 L513 150 L0 150 Z" fill="url(#lhRed)"/>
    <path d="M0 20 C150 60 330 100 513 50" fill="none" stroke="#fff" stroke-opacity=".35" stroke-width="2"/>
  </svg>
  <p class="address">Merelhoflaan 20<br>3712 KL Lindeveld<br>T 030 123 4567 | F 030 765 4321<br>info@lindeveldwerkplaats.nl | www.lindeveldwerkplaats.nl</p>
</section>

<section class="piece card card-front" aria-label="Visitekaartje voorzijde">
  <div class="brand"><span class="mark"></span><span>Motorwerkplaats Lindeveld</span></div>
  <p class="person">Ruben Verhoek</p>
  <p class="contact">Merelhoflaan 20<br>3712 KL Lindeveld<br>T 030 123 4567<br>F 030 765 4321<br>info@lindeveldwerkplaats.nl</p>
  <svg class="wave" viewBox="0 0 216 42" preserveAspectRatio="none" aria-hidden="true">
    <path d="M0 30 C70 40 150 30 216 4 L216 42 L0 42 Z" fill="var(--red)"/>
  </svg>
</section>

<section class="piece card card-red" aria-label="Visitekaartje achterzijde rood">
  <div class="brand on-dark"><span class="mark"></span><span>Motorwerkplaats Lindeveld</span></div>
  <ul class="services"><li>- Onderhoud - APK</li><li>- Banden - Airco</li><li class="all">Voor alle merken</li></ul>
</section>

<section class="piece card card-white" aria-label="Visitekaartje achterzijde wit">
  <div class="brand"><span class="mark"></span><span>Motorwerkplaats Lindeveld</span></div>
  <ul class="services"><li>- Onderhoud - APK</li><li>- Banden - Airco</li><li class="all">Voor alle merken</li></ul>
</section>

<section class="piece card card-grey" aria-label="Visitekaartje achterzijde grijs">
  <div class="brand"><span class="mark"></span><span>Motorwerkplaats Lindeveld</span></div>
  <ul class="services"><li>- Onderhoud</li><li>- APK</li><li>- Banden</li><li>- Airco</li><li class="all">Voor alle merken</li></ul>
</section>

<section class="piece envelope" aria-label="Envelop">
  <svg class="flap" viewBox="0 0 545 140" preserveAspectRatio="none" aria-hidden="true">
    <defs><linearGradient id="envRed" x1="0" y1="0" x2="0" y2="1"><stop offset="0" stop-color="#8c0d12"/><stop offset=".6" stop-color="#c4161c"/><stop offset="1" stop-color="#e33a3f"/></linearGradient></defs>
    <rect width="545" height="140" fill="url(#envRed)"/>
    <path d="M0 140 C120 100 200 70 272 70 C345 70 425 100 545 140 Z" fill="var(--paper)"/>
  </svg>
  <div class="brand on-dark flap-name"><span class="mark"></span><span>Motorwerkplaats Lindeveld</span></div>
  <div class="brand sender"><span class="mark"></span><span>Motorwerkplaats Lindeveld</span></div>
  <p class="address">Merelhoflaan 20<br>3712 KL Lindeveld</p>
  <svg class="wave" viewBox="0 0 545 70" preserveAspectRatio="none" aria-hidden="true">
    <path d="M0 60 C200 70 400 50 545 0 L545 70 L0 70 Z" fill="var(--red)"/>
  </svg>
</section>

</body>
</html>
```